Water ATM Card

Need a design for water ATM cards. Size of card is 3.375 x 2.125 inch
On the Front include the Cedar brook Logo.
Bottom right corner should have Price $100
On the Back
This card is to be used to access water refills at any Cedar Brook Water Vending Machines.
Please contact (869) 614 2938 or (869) 731 4072 or email clearflowhq@examplemail.com for any assistance or recharging of card.

```html
<!DOCTYPE html>
<html lang="en">
<head>
<meta charset="utf-8">
<title>Cedar Brook Water Card</title>
<link href="https://fonts.googleapis.com/css2?family=Montserrat:wght@400;600;700&display=swap" rel="stylesheet">
<style>
  :root {
    --backdrop: #adadad;
    --card: #ffffff;
    --brand-blue: #1a6fb5;
    --soft-green: #dcecc8;
    --soft-mint: #cfe6d6;
    --soft-blue: #c6d8ea;
  }
  * { margin: 0; padding: 0; box-sizing: border-box; }
  html, body {
    width: 1200px; height: 1000px; overflow: hidden;
    background: var(--backdrop);
    font-family: "Montserrat", Arial, sans-serif;
    color: var(--brand-blue);
  }
  .card {
    position: absolute;
    left: 294px;
    width: 615px;
    height: 352px;
    background: var(--card);
    overflow: hidden;
  }
  .card--front { top: 78px; }
  .card--back { top: 483px; width: 613px; }

  .brand {
    position: absolute; left: 0; right: 0; top: 180px;
    text-align: center;
  }
  .brand__name {
    font-weight: 700; font-size: 31px; letter-spacing: 0.5px; line-height: 1;
  }
  .brand__tagline {
    font-weight: 400; font-size: 18px; margin-top: 6px; line-height: 1;
  }
  .price {
    position: absolute; left: 0; right: 0; top: 262px;
    display: flex; justify-content: center; align-items: center; gap: 8px;
  }
  .price__amount { font-weight: 700; font-size: 50px; line-height: 1; letter-spacing: -1px; }
  .price__label { font-weight: 700; font-size: 21px; line-height: 0.95; }

  .back__decoration {
    position: absolute; right: 0; bottom: 0; width: 470px; height: 230px;
    background: linear-gradient(100deg, rgba(255,255,255,0) 0%, var(--soft-green) 55%, var(--soft-mint) 75%, var(--soft-blue) 100%);
    -webkit-mask-image: linear-gradient(to top, #000 30%, transparent 100%);
            mask-image: linear-gradient(to top, #000 30%, transparent 100%);
    opacity: 0.85;
  }
  .back__intro {
    position: absolute; left: 39px; top: 94px;
    font-size: 18px; line-height: 22px; font-weight: 400;
  }
  .back__intro strong { font-weight: 700; }
  .contacts {
    position: absolute; left: 39px; top: 188px; list-style: none;
  }
  .contacts__item {
    display: flex; align-items: center; gap: 10px;
    font-size: 21px; line-height: 25.5px;
  }
  .contacts__icon { width: 20px; height: 20px; flex: none; fill: var(--brand-blue); }
  .back__note {
    position: absolute; left: 40px; top: 273px;
    font-size: 10.5px; letter-spacing: 0.4px; text-transform: uppercase;
  }
</style>
</head>
<body>
  <section class="card card--front" aria-label="Card front">
    <div class="brand">
      <div class="brand__name">CEDAR BROOK</div>
      <div class="brand__tagline">Purified Spring Water</div>
    </div>
    <div class="price">
      <span class="price__amount">$100</span>
      <span class="price__label">WATER<br>REFILLS</span>
    </div>
  </section>

  <section class="card card--back" aria-label="Card back">
    <div class="back__decoration" role="img" aria-label="Faint brand decoration in soft green and blue tones"></div>
    <p class="back__intro">This card is to be used to access<br>water refills at any <strong>Cedar Brook<br>Water Vending Machines.</strong></p>
    <ul class="contacts">
      <li class="contacts__item">
        <svg class="contacts__icon" viewBox="0 0 24 24" aria-hidden="true"><path d="M6.6 10.8a15.1 15.1 0 0 0 6.6 6.6l2.2-2.2a1 1 0 0 1 1-.25 11.4 11.4 0 0 0 3.6.57 1 1 0 0 1 1 1V20a1 1 0 0 1-1 1A17 17 0 0 1 3 4a1 1 0 0 1 1-1h3.5a1 1 0 0 1 1 1c0 1.25.2 2.45.57 3.57a1 1 0 0 1-.25 1z"/></svg>
        (869) 614 2938
      </li>
      <li class="contacts__item">
        <svg class="contacts__icon" viewBox="0 0 24 24" aria-hidden="true"><path d="M6.6 10.8a15.1 15.1 0 0 0 6.6 6.6l2.2-2.2a1 1 0 0 1 1-.25 11.4 11.4 0 0 0 3.6.57 1 1 0 0 1 1 1V20a1 1 0 0 1-1 1A17 17 0 0 1 3 4a1 1 0 0 1 1-1h3.5a1 1 0 0 1 1 1c0 1.25.2 2.45.57 3.57a1 1 0 0 1-.25 1z"/></svg>
        (869) 731 4072
      </li>
      <li class="contacts__item">
        <svg class="contacts__icon" viewBox="0 0 24 24" aria-hidden="true"><path d="M2 6h20v13H2z M2 6l10 7 10-7" fill="var(--brand-blue)"/><path d="M2.5 6.5l9.5 6.6 9.5-6.6" fill="none" stroke="#fff" stroke-width="1.4"/></svg>
        clearflowhq@examplemail.com
      </li>
    </ul>
    <p class="back__note">For any assistance or recharging&nbsp; of card.</p>
  </section>
</body>
</html>
```